Medical Device - Case Study Template

We need a TEMPLATE that we can reuse to write various case studies about the medical equipment solutions we provide. It will be a double sided letter sized with a modern design that conveys a feeling of expertise, innovation and highly personable service AND be consistent with the brand guide. The content will be divided into a few sections:

- Situation (200-250 words)
- Challenge (100-120 words)
- Solution (100-120 words)
- Results (100-120 words)
- Conclusion (100-120 words)

Additionally, there will need to be a call to action, inviting people to send an email for more information and a short "About Valtu" section (approx. 40 words).

For device picture placeholders, feel free to use any random small benchtop medical device.

```html
<!DOCTYPE html>
<html lang="en">
<head>
<meta charset="utf-8">
<title>Valtu Case Study Template</title>
<link rel="stylesheet" href="https://fonts.googleapis.com/css2?family=Fira+Sans+Extra+Condensed:wght@600;700&family=Source+Sans+3:wght@400;600;700&display=swap">
<style>
:root{
  --stage:#1d1d1f;
  --paper:#ffffff;
  --green:#8bd64a;
  --green-deep:#74c23a;
  --green-pale:#dff3cf;
  --orange:#ee7d2c;
  --orange-deep:#d96a1c;
  --orange-soft:#f28a3a;
  --ink:#2b2b2b;
  --body:#3a3a3a;
  --teal-grey:#5f8f96;
  --ice:#cfe6f5;
  --ice-deep:#8cc3e8;
}
*{box-sizing:border-box;margin:0;padding:0}
html,body{width:1200px;height:840px;overflow:hidden;background:var(--stage)}
body{position:relative;font-family:"Source Sans 3",Arial,sans-serif;color:var(--body)}
.page{position:absolute;top:85px;width:519px;height:670px;background:var(--paper);overflow:hidden}
.page--front{left:68px}
.page--back{left:614px}
.abs{position:absolute}
.heading{font-family:"Fira Sans Extra Condensed","Arial Narrow",sans-serif;font-weight:600;color:var(--orange);font-size:22px;line-height:1;display:flex;align-items:center;gap:6px}
.heading svg{width:24px;height:24px;flex:none}
.copy{font-size:8.1px;line-height:10.7px;color:var(--body)}
.copy p+p{margin-top:10.7px}

/* front */
.hero-bg{left:0;top:0;width:519px;height:420px;background:linear-gradient(135deg,var(--green-deep) 0%,var(--green) 28%,#c9ecaa 55%,#ffffff 78%)}
.hero-photo{left:300px;top:140px;width:219px;height:280px;background:radial-gradient(ellipse at 60% 40%,#9fd9b8 0%,#c7ecc9 45%,rgba(255,255,255,0) 80%)}
.hero-fade{left:0;top:200px;width:519px;height:440px;background:linear-gradient(180deg,rgba(255,255,255,0) 0%,rgba(255,255,255,.75) 10%,rgba(232,246,220,.6) 55%,#ffffff 100%)}
.title-panel{left:0;top:0;width:329px;height:201px;background:var(--green-deep);border-bottom-right-radius:6px;opacity:.85}
.hero-tiles .tile{position:absolute;background:rgba(255,255,255,.55)}
.title{left:48px;top:84px;width:290px;font-family:"Fira Sans Extra Condensed","Arial Narrow",sans-serif;font-weight:600;font-size:23.5px;line-height:31px;color:var(--ink)}
.brand{display:flex;align-items:center;gap:7px;font-family:"Source Sans 3",Arial,sans-serif;font-weight:600;font-size:26px;letter-spacing:.5px}
.brand-dot{width:22px;height:22px;border-radius:50%;flex:none}
.brand--front{left:338px;top:22px;color:var(--teal-grey)}
.brand--front .brand-dot{background:var(--orange)}
.footer{left:0;top:642px;width:519px;height:28px;background:var(--orange);color:#fff;font-weight:700;font-size:9px;display:flex;align-items:center;justify-content:flex-end;padding-right:47px;letter-spacing:.2px}

/* back */
.masthead{left:0;top:0;width:519px;height:72px;background:var(--green)}
.brand--back{left:46px;top:22px;color:#fff}
.brand--back .brand-dot{background:#fff}
.photo{position:absolute;width:122px}
.about-band{left:0;top:478px;width:519px;height:164px;background:var(--orange)}
.about-title{left:48px;top:492px;font-family:"Fira Sans Extra Condensed","Arial Narrow",sans-serif;font-weight:600;font-size:15px;color:#fff}
.about-copy{left:48px;top:519px;width:200px;color:#fff}
.contacts{left:18px;top:593px;width:492px;display:flex;justify-content:space-between;color:#fff;font-size:8px;text-align:center}
.contact{width:118px;display:flex;flex-direction:column;align-items:center;gap:3px;line-height:9px}
.contact svg{width:14px;height:14px}
.contact b{font-weight:700}
.footer--back{border-top:1px solid rgba(255,255,255,.35);background:var(--orange-soft)}
</style>
</head>
<body>

<section class="page page--front">
  <div class="abs hero-bg"></div>
  <div class="abs hero-photo" role="img" aria-label="Soft green medical photo of a stethoscope over a heart-rate chart"></div>
  <div class="abs hero-fade"></div>
  <div class="abs title-panel"></div>
  <div class="abs hero-tiles">
    <div class="tile" style="left:400px;top:125px;width:72px;height:76px"></div>
    <div class="tile" style="left:400px;top:201px;width:119px;height:51px;background:rgba(255,255,255,.75)"></div>
    <div class="tile" style="left:472px;top:252px;width:47px;height:62px;background:rgba(255,255,255,.85)"></div>
  </div>
  <div class="abs brand brand--front"><span class="brand-dot"></span>Valtu</div>
  <h1 class="abs title">Lorem Ipsum Dolor Sit Ametconsectetur Adipiscing Etiam Convallis Leo Risuravida</h1>

  <h2 class="abs heading" style="left:48px;top:221px">
    <svg viewBox="0 0 24 24" fill="none" stroke="currentColor" stroke-width="1.4"><circle cx="7" cy="8" r="3"/><circle cx="17" cy="8" r="3"/><circle cx="12" cy="13" r="3"/><path d="M2 21c0-4 2-6 5-6M22 21c0-4-2-6-5-6M7 22c0-3 2-5 5-5s5 2 5 5"/></svg>
    Situation
  </h2>
  <div class="abs copy" style="left:48px;top:251px;width:203px">
    <p>Lorem ipsum dolor sit amet, consectetur adipiscing elit. Etiam convallis leo risus, vel gravida quam bibendum aliquet. Pellentesque enim ipsum, facilisis vel mattis a, scelerisque in metus. Praesent vitae mauris ex. Sed lacinia justo sed massa dictum, nec ultrices tellus euismod. Donec et blandit felis, in mattis felis. Aliquam non enim eu metus bibendum dapibus. Nunc hendrerit ante id risus convallis pellentesque. Donec hendrerit leo eget libero commodo, eu consectetur neque tristique. Suspendisse eget eros scelerisque, dictum nunc vel, maximus risus. Vestibulum enim erat, consequat quis diam nec, pellentesque sagittis nibh. Curabitur efficitur imperdiet mattis. Donec maximus nunc id imperdiet tincidunt. Sed pulvinar, elit non ullamcorper venenatis, dolor risus venenatis nisl, nec ultrices odio sem in erat.</p>
    <p>Pellentesque commodo ipsum nec felis dignissim rutrum. Curabitur accumsan neque a lectus varius, ut dapibus dui ultricies. Donec quis eros aliquam, venenatis mi ac, molestie libero. Etiam eget lectus quam. Curabitur eget laoreet mi, vitae facilisis sapien. Sed vitae nisl sit amet lectus vestibulum dapibus sed ac risus. Nam dictum faucibus aliquet. Duis euismod nisl in massa imperdiet pretium et nec diam. Donec eget porta diam.</p>
    <p>Quisque faucibus justo ligula, quis mattis nisi blandit nec. Duis dolor nibh, auctor et tortor eget, auctor blandit odio. Ut sapien elit, pharetra ut ante quis, imperdiet fermentum leo. Nulla aliquam interdum nibh at hendrerit. Morbi interdum sed est ac egestas. Maecenas convallis magna vel purus volutpat, vel vehicula est dignissim. Sed convallis efficitur viverra. Sed tincidunt tristique massa id sodales. Sed ut ipsum sed nunc vehicula.</p>
  </div>

  <h2 class="abs heading" style="left:271px;top:411px">
    <svg viewBox="0 0 24 24" fill="none" stroke="currentColor" stroke-width="1.4"><circle cx="15" cy="8" r="4"/><circle cx="15" cy="8" r="1.5"/><path d="M2 22V14l5-2 4 3 6-2v9z"/></svg>
    <span style="margin-left:8px">Challenge</span>
  </h2>
  <div class="abs copy" style="left:271px;top:446px;width:203px">
    <p>Lorem ipsum dolor sit amet, consectetur adipiscing elit. Phasellus posuere tincidunt egestas. In enim lacus, rhoncus posuere eros ultricies, condimentum suscipit elit. Sed fermentum ligula leo, sed bibendum nisi mattis sed. Vestibulum vestibulum dolor eget ipsum vulputate, vel sollicitudin erat tempus. Fusce eleifend enim dui, sed gravida tortor lobortis nec. Ut mi leo, viverra at nisl in, mattis dictum mauris. Cras porta elit eget facilisis varius. Nulla sit amet tempor leo, quis aliquam neque. Quisque ultricies egestas dui, non posuere arcu dignissim ac. Ut eu leo id nulla tincidunt molestie. Mauris facilisis porttitor neque, a pulvinar leo efficitur eu. Nam auctor magna tincidunt quam sollicitudin, eu tempor arcu mollis. Mauris dapibus urna sit amet augue tempus pellentesque. Aliquam a nulla.</p>
  </div>

  <div class="abs footer">www.valtu.com</div>
</section>

<section class="page page--back">
  <div class="abs masthead"></div>
  <div class="abs brand brand--back"><span class="brand-dot"></span>Valtu</div>

  <h2 class="abs heading" style="left:48px;top:78px">
    <svg viewBox="0 0 24 24" fill="none" stroke="currentColor" stroke-width="1.4"><path d="M8 16a6 6 0 1 1 8 0v3H8z"/><path d="M9 22h6M12 8v6M9 11h6M12 1v2M3 10H1M23 10h-2M5 4 4 3M19 4l1-1"/></svg>
    Solution
  </h2>
  <div class="abs copy" style="left:48px;top:110px;width:203px">
    <p>Lorem ipsum dolor sit amet, consectetur adipiscing elit. Phasellus posuere tincidunt egestas. In enim lacus, rhoncus posuere eros ultricies, condimentum suscipit elit. Sed fermentum ligula leo, sed bibendum nisi mattis sed. Vestibulum vestibulum dolor eget ipsum vulputate, vel sollicitudin erat tempus. Fusce eleifend enim dui, sed gravida tortor lobortis nec. Ut mi leo, viverra at nisl in, mattis dictum mauris. Cras porta elit eget facilisis varius. Nulla sit amet tempor leo, quis aliquam neque. Quisque ultricies egestas dui, non posuere arcu dignissim ac. Ut eu leo id nulla tincidunt molestie. Mauris facilisis porttitor neque, a pulvinar leo efficitur eu. Nam auctor magna tincidunt quam sollicitudin, eu tempor arcu mollis. Mauris dapibus urna sit amet augue tempus pellentesque. Aliquam a nulla.</p>
  </div>

  <h2 class="abs heading" style="left:271px;top:78px">
    <svg viewBox="0 0 24 24" fill="none" stroke="currentColor" stroke-width="1.4"><path d="M4 2h12v20H4z"/><path d="M7 6h6M7 10h6M7 14h3"/><circle cx="18" cy="17" r="4"/><path d="m16 17 1.5 1.5L20 16"/></svg>
    <span style="margin-left:6px">Results</span>
  </h2>
  <div class="abs copy" style="left:271px;top:110px;width:203px">
    <p>Lorem ipsum dolor sit amet, consectetur adipiscing elit. Phasellus posuere tincidunt egestas. In enim lacus, rhoncus posuere eros ultricies, condimentum suscipit elit. Sed fermentum ligula leo, sed bibendum nisi mattis sed. Vestibulum vestibulum dolor eget ipsum vulputate, vel sollicitudin erat tempus. Fusce eleifend enim dui, sed gravida tortor lobortis nec. Ut mi leo, viverra at nisl in, mattis dictum mauris. Cras porta elit eget facilisis varius. Nulla sit amet tempor leo, quis aliquam neque. Quisque ultricies egestas dui, non posuere arcu dignissim ac. Ut eu leo id nulla tincidunt molestie. Mauris facilisis porttitor neque, a pulvinar leo efficitur eu. Nam auctor magna tincidunt quam sollicitudin, eu tempor arcu mollis. Mauris dapibus urna sit amet augue tempus pellentesque. Aliquam a nulla.</p>
  </div>

  <h2 class="abs heading" style="left:48px;top:272px">
    <svg viewBox="0 0 24 24" fill="none" stroke="currentColor" stroke-width="1.4"><path d="m12 1 1 2 2 .3-1.5 1.4.4 2L12 5.7 10.1 6.7l.4-2L9 3.3l2-.3z"/><circle cx="12" cy="10" r="2"/><path d="M2 8l5 6h10l5-6M8 14l-2 8M16 14l2 8M9 14v8h6v-8"/></svg>
    Conclusion
  </h2>
  <div class="abs copy" style="left:48px;top:305px;width:203px">
    <p>Lorem ipsum dolor sit amet, consectetur adipiscing elit. Phasellus posuere tincidunt egestas. In enim lacus, rhoncus posuere eros ultricies, condimentum suscipit elit. Sed fermentum ligula leo, sed bibendum nisi mattis sed. Vestibulum vestibulum dolor eget ipsum vulputate, vel sollicitudin erat tempus. Fusce eleifend enim dui, sed gravida tortor lobortis nec. Ut mi leo, viverra at nisl in, mattis dictum mauris. Cras porta elit eget facilisis varius. Nulla sit amet tempor leo, quis aliquam neque. Quisque ultricies egestas dui, non posuere arcu dignissim ac. Ut eu leo id nulla tincidunt molestie. Mauris facilisis porttitor neque, a pulvinar leo efficitur eu. Nam auctor magna tincidunt quam sollicitudin, eu tempor arcu mollis. Mauris dapibus urna sit amet augue tempus pellentesque. Aliquam a nulla.</p>
  </div>

  <div class="abs about-band"></div>

  <div class="photo" style="left:270px;top:285px;height:58px;background:#ececec"></div>
  <div class="photo" role="img" aria-label="Gloved hand filling a syringe from a vial" style="left:397px;top:285px;height:58px;background:linear-gradient(135deg,#6aa6d6,#cfe3f1 55%,#eef4f8)"></div>
  <div class="photo" role="img" aria-label="Two syringes with orange plungers on grey surface" style="left:270px;top:347px;height:64px;background:linear-gradient(135deg,#9a9a9a,#c4c4c4 60%,#b0b0b0)"></div>
  <div class="photo" role="img" aria-label="Blue dental chair headrest" style="left:397px;top:347px;height:64px;background:linear-gradient(135deg,var(--ice-deep),var(--ice))"></div>
  <div class="photo" role="img" aria-label="Dental treatment unit in blue light" style="left:270px;top:415px;height:63px;background:linear-gradient(160deg,#a9d4f1,#5fa9de)"></div>
  <div class="photo" role="img" aria-label="Close view of a dental chair and lamp" style="left:397px;top:415px;height:63px;background:linear-gradient(200deg,#d7ebf8,#6fb2e2)"></div>
  <div class="photo" style="left:270px;top:482px;height:65px;background:var(--orange-deep)"></div>
  <div class="photo" role="img" aria-label="Modern dental surgery room with equipment" style="left:397px;top:482px;height:65px;background:linear-gradient(135deg,#e6e6e6,#9c9c9c 60%,#5a5a5a)"></div>
  <div class="photo" style="left:397px;top:547px;height:68px;background:var(--orange-soft)"></div>

  <h2 class="abs about-title">About Valtu</h2>
  <p class="abs copy about-copy">Lorem ipsum dolor sit amet, consectetur adipiscing elit. Proin mauris erat, vehicula egestas lectus a, elementum pharetra nisl. Pellentesque in rutrum justo, et venenatis orci. Curabitur ut accumsan erat. Praesent sit amet tellus quis nibh commodo dapibus. Vivamus venenatis ut.</p>

  <div class="abs contacts">
    <div class="contact">
      <svg viewBox="0 0 24 24"><circle cx="12" cy="12" r="12" fill="#fff"/><path d="M12 5a4.5 4.5 0 0 0-4.5 4.5C7.5 13 12 19 12 19s4.5-6 4.5-9.5A4.5 4.5 0 0 0 12 5z" fill="var(--orange)"/><circle cx="12" cy="9.5" r="1.6" fill="#fff"/></svg>
      <span><b>Head Office</b><br>12 Lorem Ipsum Plaza</span>
    </div>
    <div class="contact">
      <svg viewBox="0 0 24 24"><circle cx="12" cy="12" r="12" fill="#fff"/><path d="M8 6l2 0 1 3-1.5 1a7 7 0 0 0 4 4l1-1.5 3 1v2c0 1-1 1.5-2 1.5A10 10 0 0 1 6.5 8C6.5 7 7 6 8 6z" fill="var(--orange)"/></svg>
      <b>(+1) 555-014-2290</b>
    </div>
    <div class="contact">
      <svg viewBox="0 0 24 24"><circle cx="12" cy="12" r="12" fill="#fff"/><rect x="7" y="7" width="10" height="11" rx="1" fill="var(--orange)"/><path d="M9 10h6M9 12.5h6M9 15h4" stroke="#fff" stroke-width="1"/></svg>
      <b>555-014-2291</b>
    </div>
    <div class="contact">
      <svg viewBox="0 0 24 24"><circle cx="12" cy="12" r="12" fill="#fff"/><path d="M6 12 18 6l-3 12-3-4-3 2 1-4z" fill="var(--orange)"/></svg>
      <b>info@valtu.com</b>
    </div>
  </div>

  <div class="abs footer footer--back">www.valtu.com</div>
</section>

</body>
</html>
```